Course flyer - evolutive design

We want to have a nice design for our course programm.
In fact we are school language, and our course programm change approximatively each 2 weeks§.
For that we need a design that we can modify each 2 weeks (only dates change ) by ourselves.
We used to have a classical design but we want to upgrade it with a modern and attractive design.
We can have 3 versions one for each city.
We have 3 offices: Tunis, Sousse & Sfax
Attached you can find old designs

Target Market(s)

students from 16 years old till retired people 76 years old

Industry/Entity Type

Education

Font styles to use
Sans Serif

Requirements
Must have
• clear timing for courses (date, days, timing)
• prices
• Adresse (each flyer has its own adress)
• phone Number
• Cool image
Should not have
• Racism
• Violence
• Too much stuff

```html
<!DOCTYPE html>
<html lang="fr">
<head>
<meta charset="utf-8">
<title>Cours d'allemand – Tunis</title>
<link rel="stylesheet" href="https://fonts.googleapis.com/css2?family=Oswald:wght@500;600&family=Roboto+Condensed:wght@400;700&family=Jost:wght@600;700&display=swap">
<style>
  :root{
    --lime:#c2d62c;
    --lime-soft:#eef4cf;
    --navy:#27384a;
    --ink:#1f1f1f;
    --green-text:#3b9d3a;
    --white:#ffffff;
    --stage:#e6e6e6;
  }
  *{margin:0;padding:0;box-sizing:border-box}
  html,body{width:1125px;height:1200px;overflow:hidden}
  body{background:var(--stage);position:relative;font-family:"Roboto Condensed",sans-serif;color:var(--ink)}
  .flyer{position:absolute;left:174px;top:52px;width:778px;height:1095px;overflow:hidden;
    background:linear-gradient(180deg,#ffffff 0%,var(--lime-soft) 55%,#f7fae8 100%)}
  .photo{position:absolute;left:0;top:0;width:778px;height:470px;
    background:linear-gradient(160deg,#6f8f4a 0%,#b9b08f 35%,#d9cbb4 60%,#9aa58a 100%)}
  .shapes{position:absolute;left:0;top:0}
  .logo-disc{position:absolute;left:-6px;top:367px;width:224px;height:224px;border-radius:50%;background:var(--white);
    display:flex;align-items:center;justify-content:center;box-shadow:0 2px 8px rgba(0,0,0,.15)}
  .logo-name{font-family:"Roboto Condensed",sans-serif;font-weight:700;font-size:40px;color:var(--navy);margin-left:40px}
  .title-box{position:absolute;left:384px;top:387px;width:337px;height:211px;background:var(--navy);color:var(--white);
    text-align:center;font-family:"Oswald",sans-serif}
  .title-box .line{font-size:35px;font-weight:500;line-height:42px}
  .title-box .first{margin-top:22px}
  .title-box .rule{width:274px;margin:8px auto 6px;border-top:2px dashed rgba(255,255,255,.75)}
  .title-box .city{font-family:"Jost",sans-serif;font-weight:700;font-size:62px;line-height:70px;letter-spacing:2px}
  .t{position:absolute;white-space:nowrap}
  .head{font-size:22px;color:var(--green-text)}
  .date{font-family:"Jost",sans-serif;font-weight:700;font-size:23px;letter-spacing:.5px}
  .slot{font-family:"Jost",sans-serif;font-weight:700;font-size:18px;color:var(--green-text)}
  .slot.big{font-size:20px}
  .list{font-size:17.5px;line-height:25px}
  .list b{font-weight:700}
  .address{position:absolute;left:402px;top:895px;width:376px;height:142px;background:var(--lime);border-radius:14px 0 0 14px;
    box-shadow:0 4px 8px rgba(0,0,0,.15)}
  .address .bar{position:absolute;left:339px;top:0;width:4px;height:142px;background:var(--navy)}
  .address .city{position:absolute;left:36px;top:12px;font-weight:700;font-size:20px;color:var(--navy)}
  .address .lines{position:absolute;left:36px;top:38px;font-size:19px;line-height:24px;color:var(--navy);white-space:nowrap}
  .address svg{position:absolute;left:16px;top:44px}
  .footer{position:absolute;left:0;top:1053px;width:778px;height:42px}
  .footer .item{position:absolute;top:10px;font-weight:700;font-size:18px;line-height:22px;color:var(--navy);display:flex;align-items:center;gap:8px;white-space:nowrap}
  .footer .web{color:var(--white)}
</style>
</head>
<body>
<main class="flyer">
  <div class="photo" role="img" aria-label="Photo : une étudiante souriante tenant des cahiers devant un campus, avec trois étudiants qui discutent en arrière-plan"></div>

  <svg class="shapes" width="778" height="700" viewBox="0 0 778 700" aria-hidden="true">
    <polygon points="0,470 170,400 384,430 384,600 240,560 0,600" fill="#ffffff"/>
    <polygon points="170,470 384,420 384,560 230,540" fill="#c2d62c"/>
    <polygon points="384,598 350,580 384,560" fill="#1a2733"/>
    <polygon points="721,380 778,370 778,605 721,598" fill="#c2d62c"/>
  </svg>

  <div class="logo-disc"><span class="logo-name">Lernwerk</span></div>

  <section class="title-box">
    <div class="line first">COURS D'ALLEMAND</div>
    <div class="line">AVRL / MAI - 2016</div>
    <div class="rule"></div>
    <div class="city">TUNIS</div>
  </section>

  <div class="t head" style="left:66px;top:642px">Extensif Lundi/Mercredi/Vendredi</div>
  <div class="t date" style="left:66px;top:672px">25/04/2016 - 20/05/2016</div>
  <div class="t slot big" style="left:66px;top:706px">18H30</div>
  <div class="t slot big" style="left:191px;top:706px">21H3O</div>
  <div class="t list" style="left:66px;top:736px"><b>A1.1</b> DK2136<br><b>A1.2</b> DK2137<br><b>A2.1</b> Dk2138</div>
  <div class="t list" style="left:191px;top:736px"><b>A2.2</b> Dk2139<br><b>B1.1</b> DK2140<br><b>B1.2</b> DK2141</div>

  <div class="t head" style="left:66px;top:829px">Intensif Lundi - Vendredi</div>
  <div class="t date" style="left:66px;top:859px">18/04/2016 - 06/05/2016</div>
  <div class="t slot" style="left:66px;top:894px">09H30 - 12H30</div>
  <div class="t slot" style="left:219px;top:894px">13H00 - 16H00</div>
  <div class="t list" style="left:66px;top:922px"><b>A1.1</b> DK2127<br><b>A1.2</b> DK2128<br><b>A2.1</b> DK2129<br><b>A2.2</b> DK2130<br><b>B1.1</b> DK2131</div>
  <div class="t list" style="left:219px;top:922px"><b>A1.1</b> DK2132<br><b>B1.2</b> DK2133<br><b>B2.1</b> DK2134<br><b>B2.2</b> Dk2135</div>

  <div class="t head" style="left:425px;top:642px">Intensif Lundi - Vendredi</div>
  <div class="t date" style="left:425px;top:670px">09/05/2016 - 27/05/2016</div>
  <div class="t slot" style="left:425px;top:707px">09H30 - 12H30</div>
  <div class="t slot" style="left:576px;top:707px">13H00 - 16H00</div>
  <div class="t list" style="left:425px;top:737px;line-height:23.5px"><b>A1-1</b> DK2142<br><b>A1-2</b> DK2143<br><b>A2-1</b> DK2144<br><b>A2-2</b> DK2145<br><b>B1.1</b> DK2146<br><b>B1.2</b> DK2147</div>
  <div class="t list" style="left:576px;top:737px;line-height:23.5px"><b>A1.1</b> DK2148<br><b>A1.2</b> DK2149<br><b>B2.1</b> Dk2150<br><b>B2.2</b> Dk2151</div>

  <section class="address">
    <div class="bar"></div>
    <div class="city">TUNIS</div>
    <svg width="14" height="18" viewBox="0 0 14 18" aria-hidden="true"><circle cx="7" cy="6" r="4" fill="none" stroke="#27384a" stroke-width="2"/><path d="M7 10v7M3 17h8" stroke="#27384a" stroke-width="2"/></svg>
    <div class="lines">Imm. les Palmiers, 2éme étage<br>8 Rue du Lac Victoria<br>(en face de la Place Jasmin)<br>1053 Les Berges du Lac 1</div>
  </section>

  <footer class="footer">
    <svg width="778" height="42" viewBox="0 0 778 42" aria-hidden="true" style="position:absolute;left:0;top:0">
      <polygon points="0,0 502,0 477,42 0,42" fill="#c2d62c"/>
      <polygon points="502,0 778,0 778,42 477,42" fill="#27384a"/>
    </svg>
    <div class="item" style="left:56px">
      <svg width="16" height="16" viewBox="0 0 16 16" aria-hidden="true"><path d="M4 1l3 4-2 2c1 2 2 3 4 4l2-2 4 3-2 3C7 15 1 9 1 3z" fill="none" stroke="#27384a" stroke-width="1.6"/></svg>
      +216 71 480 316
    </div>
    <div class="item" style="left:255px">
      <svg width="18" height="13" viewBox="0 0 18 13" aria-hidden="true"><rect x="1" y="1" width="16" height="11" fill="none" stroke="#27384a" stroke-width="1.6"/><path d="M1 1l8 6 8-6" fill="none" stroke="#27384a" stroke-width="1.6"/></svg>
      tunis@lernwerk.org
    </div>
    <div class="item web" style="left:548px">
      <svg width="16" height="16" viewBox="0 0 16 16" aria-hidden="true"><circle cx="8" cy="8" r="7" fill="none" stroke="#ffffff" stroke-width="1.5"/><path d="M1 8h14M8 1c-3 4-3 10 0 14M8 1c3 4 3 10 0 14" fill="none" stroke="#ffffff" stroke-width="1.3"/></svg>
      www.lernwerk.org
    </div>
  </footer>
</main>
</body>
</html>
```